Financial Services - Brochure for Mortgage Brokers to use with Borrowers

******** Modification - based on the designs we have received to date we have decided to go with 11x17" (4 faces) that will be folded into 8.5x11 - we have too much information for the smaller tri-fold format. ***************

We need to develop a tool for mortgage brokers (our distribution channel) to use with borrowers to make selling our services easier.

Our brochure will be in both english and french (probably 2 separate units due to length) (to date our collateral materials have been one page recto-verso with english on one side and french on the other side).

We already have a layout that we use - see examples for existing layout and design format (i will upload the: 1) 8.5'x11' single page flyer with english on e side and french the other side 2) the 10 questions unit we use 4.5"x11")

I have prepared a powerpoint which I will upload that shows the objectives and provides content examples.

The final product we are looking for is in English, we would then provide the french text to add to the 2nd unit.

Reason: I have been traveling and not able to respond to submissions. I would like to provide time for feedback.

Clarification:

We are open to 2 formats: either 8.5x11" trifold or 11x17" brochure (4 faces) format. 

Reason: Still traveling and need time to finalize feedback - thank you

Target Market(s)

Borrowers (consumers) who are having financial difficulties and as a result may lose their homes - they are in a high state of emotional crisis and need someone to "take charge (broker)" and be walked thru a plan (our brochure that you will be creating)

Industry/Entity Type

Financial

Requirements
Must have
• Must be consistent with our current look and feel (ie colours, professionalism)

Must be easy to produce as we will do short runs and have the brochures printed with our different broker's contact info on the back - so either a trifold 8.5"x11" or a 11x17"

```html
<!DOCTYPE html>
<html lang="en">
<head>
<meta charset="utf-8">
<title>Short Term Mortgage Solutions – Brochure</title>
<link rel="stylesheet" href="https://fonts.googleapis.com/css2?family=Roboto+Condensed:wght@400;500&family=Roboto:wght@400&display=swap">
<style>
  :root {
    --purple: #675c8c;
    --purple-text: #5d5789;
    --sage: #879d9c;
    --sage-dark: #7a9190;
    --ink: #3b3b3b;
    --paper: #ffffff;
    --backdrop: #e8e6e3;
    --head: "Roboto Condensed", sans-serif;
    --body: "Roboto", sans-serif;
  }
  * { box-sizing: border-box; margin: 0; padding: 0; }
  html, body { width: 1200px; height: 960px; overflow: hidden; }
  body { background: var(--backdrop); position: relative; font-family: var(--body); color: var(--ink); }

  .brochure {
    position: absolute; left: 30px; top: 39px;
    width: 1140px; height: 882px;
    display: flex;
    background: var(--purple);
    box-shadow: 0 4px 14px rgba(0,0,0,.18);
  }
  .panel { width: 380px; height: 100%; position: relative; }
  .panel--inside { padding: 6px 8px 7px 7px; }
  .panel--inside .sheet { background: var(--paper); height: 100%; position: relative; }

  /* left panel */
  .info { padding: 36px 18px 0 20px; }
  .info h2 {
    font-family: var(--head); font-weight: 400; color: var(--purple-text);
    font-size: 29px; line-height: 34px; margin-bottom: 12px;
  }
  .info ul { list-style: none; margin-bottom: 28px; }
  .info li { font-size: 17.5px; line-height: 20px; margin-bottom: 11.5px; padding-left: 16px; text-indent: -16px; }
  .info li::before { content: ">"; display: inline-block; width: 16px; text-indent: 0; }
  .info .wrap { padding-left: 16px; text-indent: -16px; }
  .info .solution li { line-height: 26px; margin-bottom: 5px; padding-left: 10px; text-indent: -16px; }
  .info .solution li::before { width: 16px; }

  /* middle panel */
  .panel--cover-mid { background: var(--sage); color: #fff; }
  .mid-title {
    position: absolute; top: 108px; left: 0; right: 0; text-align: center;
    font-family: var(--head); font-weight: 500;
  }
  .mid-title h1 { font-size: 35px; line-height: 34px; font-weight: 500; }
  .mid-title p { font-size: 25px; margin-top: 18px; }
  .photo-couple {
    position: absolute; top: 309px; left: 0; width: 380px; height: 253px;
    background: linear-gradient(180deg, #c9cfc7 0%, #9fb08a 45%, #6f8a4f 70%, #b0634a 88%, #e9e9e6 100%);
  }
  .mid-brand {
    position: absolute; top: 660px; left: 0; right: 0;
    display: flex; align-items: center; justify-content: center; gap: 12px;
    font-family: var(--head); font-size: 34px; letter-spacing: 4px; color: var(--purple);
  }
  .mid-brand .dot { width: 22px; height: 22px; border-radius: 50%; background: var(--purple); }
  .contact {
    position: absolute; top: 758px; left: 0; right: 0; text-align: center;
    font-size: 16.5px; line-height: 21px;
  }
  .contact .lines { display: flex; justify-content: center; gap: 14px; align-items: center; }
  .contact svg { width: 14px; height: 14px; vertical-align: -2px; margin-right: 2px; }

  /* right panel */
  .photo-house {
    position: absolute; top: 0; left: 0; right: 0; height: 302px;
    background: linear-gradient(180deg, #ffffff 0%, #f3f1ee 25%, #c9b69a 55%, #9a8a74 78%, #5f7f45 100%);
  }
  .brand {
    position: absolute; top: 455px; left: 0; right: 0;
    display: flex; align-items: center; justify-content: center; gap: 14px;
    font-family: var(--head); font-size: 62px; letter-spacing: 8px; color: var(--purple);
  }
  .brand .dot { width: 26px; height: 26px; border-radius: 50%; background: var(--purple); }
  .cover-title {
    position: absolute; top: 632px; left: 0; right: 0; text-align: center;
    font-family: var(--head); font-weight: 500; font-size: 57px; line-height: 60px;
    color: var(--sage-dark);
  }
  .cover-title .accent { color: var(--purple-text); }
  .url {
    position: absolute; top: 832px; left: 0; right: 0; text-align: center;
    font-size: 16.5px; color: var(--purple-text); letter-spacing: .5px;
  }
</style>
</head>
<body>
<main class="brochure">
  <section class="panel panel--inside">
    <div class="sheet info">
      <h2>Life Happens</h2>
      <ul>
        <li>Divorce</li>
        <li>Loss of job</li>
        <li>Sickness/health</li>
        <li>Unforeseen circumstances</li>
        <li>Starting a new business</li>
      </ul>
      <h2>Creates Financial Crisis Situations</h2>
      <ul>
        <li>Notice of assessment (NOA) not paid</li>
        <li>Legal mortgage</li>
        <li>Unpaid property taxes</li>
        <li>Crack in the house foundation</li>
        <li>Construction lien</li>
        <li>Less than 2 years in business-for-self (BFS)</li>
        <li>60 day notice</li>
      </ul>
      <h2>Solution</h2>
      <ul class="solution">
        <li>Use the Equity in your home to:</li>
        <li>solve the current “financial crisis”</li>
        <li>develop and fund a plan to put you back on a solid financial footing and in good standing</li>
      </ul>
    </div>
  </section>

  <section class="panel panel--cover-mid">
    <div class="mid-title">
      <h1>SHORT TERM MORTGAGE<br>SOLUTIONS</h1>
      <p>FUNDING TO ACHIEVE YOUR GOALS™</p>
    </div>
    <div class="photo-couple" role="img" aria-label="Photo of a smiling couple embracing in front of their home with a white picket fence and brick gate posts"></div>
    <div class="mid-brand"><span class="dot"></span>CORVANE</div>
    <address class="contact" style="font-style:normal">
      Corvane Finance<br>
      42 Maple Grove Road, Suite 210<br>
      Pointe-Claire, Quebec H9R 2K7<br>
      <span class="lines">
        <span><svg viewBox="0 0 16 16" aria-hidden="true"><path fill="none" stroke="#fff" stroke-width="1.4" d="M4 1.5l2.5 3-1.5 1.8c.8 1.8 2.2 3.2 4 4l1.8-1.5 3 2.5-1.6 2.2C7.5 13.5 2.5 8.5 1.8 3.1z"/></svg>514.555.0142</span>
        <span><svg viewBox="0 0 16 16" aria-hidden="true"><rect x="4" y="1" width="8" height="5" fill="#fff"/><rect x="1" y="7" width="14" height="8" rx="1" fill="#fff"/></svg>1.800.555.0199</span>
      </span>
    </address>
  </section>

  <section class="panel panel--inside">
    <div class="sheet">
      <div class="photo-house" role="img" aria-label="Photo of a two-storey brick house with a double garage and landscaped front lawn"></div>
      <div class="brand"><span class="dot"></span>CORVANE</div>
      <h1 class="cover-title">SHORT TERM<br><span class="accent">MORTGAGE</span><br>SOLUTIONS</h1>
      <p class="url">www.corvanefinance.com</p>
    </div>
  </section>
</main>
</body>
</html>
```